Labeling for Organic Food

we need a label design for

1. Organic Red Rice
2. Organic wild honey

it is going to be the same design in different dimensions.

1. Organic Red Rice
Dimension 1 28*18.5cm
Dimension 2 13.5*8cm

2. Organic Honey
12*6cm
Updates

There is an update in the brief about using the Bhutanese color scheme. Please check it out.

Target Market(s)

people with the concern of health and the environment.

Requirements
Must have
• 1. our logo
• 2. All the info
• 3. A natural feel
• 4. I would prefer minimalistic style
• 5. Please include Bhutanese national colours as attached.

```html
<!DOCTYPE html>
<html lang="en">
<head>
<meta charset="utf-8">
<title>Greenfold – Organic Red Rice Label</title>
<link rel="stylesheet" href="https://fonts.googleapis.com/css2?family=Hind:wght@500;600&family=Signika:wght@300;400&family=Sniglet:wght@400;800&family=Noto+Sans+SC:wght@300&family=Archivo+Narrow:wght@400;700&family=Archivo+Black&display=swap">
<style>
  :root {
    --paper: #ffffff;
    --stripe: #f1f1f1;
    --gold: #f4c322;
    --gold-deep: #e2a91a;
    --ink: #161616;
    --ink-soft: #3a3a3a;
    --brown: #3b2a12;
    --red: #c8102e;
    --flag-yellow: #f5b82a;
    --flag-red: #c3161c;
  }
  * { box-sizing: border-box; margin: 0; padding: 0; }
  html, body { width: 1200px; height: 792px; overflow: hidden; background: var(--paper); }
  .label {
    position: relative; width: 1200px; height: 792px; overflow: hidden;
    background: repeating-linear-gradient(90deg, var(--paper) 0 5px, var(--stripe) 5px 6px);
    color: var(--ink);
  }
  .band { position: absolute; left: 0; width: 100%; background: var(--gold); }
  .band--top { top: 8px; height: 14px; }
  .band--bottom { top: 750px; height: 16px; }
  .band--bottom-thin { top: 772px; height: 4px; }

  .brand-tab { position: absolute; left: 398px; top: 0; width: 404px; height: 124px; }
  .brand-tab svg { position: absolute; inset: 0; }
  .brand-name {
    position: absolute; left: 0; right: 0; top: 28px; text-align: center;
    font-family: "Sniglet", sans-serif; font-weight: 800; font-size: 50px; color: var(--brown);
  }

  .info {
    position: absolute; left: 30px; width: 330px;
    font-family: "Signika", sans-serif; font-weight: 300; font-size: 19.5px; line-height: 30px; color: var(--ink);
  }
  .info--story { top: 72px; text-align: justify; }
  .info--storage { top: 320px; }
  .info--ingredients { top: 380px; }
  .info--weight { top: 470px; }
  .info--origin { top: 592px; }
  .best-before { color: var(--red); }

  .flag { position: absolute; left: 87px; top: 633px; width: 206px; height: 103px; }

  .product-title {
    position: absolute; left: 380px; width: 440px; top: 150px; text-align: center;
    font-family: "Hind", sans-serif; font-weight: 500; font-size: 86px; line-height: 92px; color: var(--ink);
  }
  .product-title-cn {
    position: absolute; left: 380px; width: 440px; top: 352px; text-align: center;
    font-family: "Noto Sans SC", sans-serif; font-weight: 300; font-size: 46px; letter-spacing: 4px;
  }
  .product-sub {
    position: absolute; left: 382px; width: 428px; top: 452px; text-align: center;
    font-family: "Sniglet", sans-serif; font-size: 38px; line-height: 46px;
  }
  .product-sub .divider { display: block; border-top: 2px dashed var(--ink); margin: 12px 10px 8px; }
  .net-weight {
    position: absolute; left: 380px; width: 440px; top: 684px; text-align: center;
    font-family: "Sniglet", sans-serif; font-size: 33px;
  }

  .nutrition {
    position: absolute; left: 907px; top: 68px; width: 244px; height: 368px;
    border: 1.5px solid var(--ink); background: var(--paper); padding: 4px 7px;
    font-family: "Archivo Narrow", sans-serif; font-size: 13px; line-height: 17px; color: var(--ink);
  }
  .nutrition__title { font-family: "Archivo Black", sans-serif; font-size: 27px; line-height: 32px; }
  .nutrition__bar { background: var(--ink); margin: 4px 0; }
  .nutrition__bar--thick { height: 12px; }
  .nutrition__bar--mid { height: 6px; }
  .nutrition__row { display: flex; justify-content: space-between; border-bottom: 1px solid var(--ink-soft); padding: 1px 0; }
  .nutrition__row--indent { padding-left: 14px; }
  .nutrition__row--plain { border-bottom: none; }
  .nutrition b { font-weight: 700; }
  .nutrition__small { font-size: 10px; line-height: 13px; }
  .nutrition__dv { text-align: right; font-size: 11px; font-weight: 700; border-bottom: 1px solid var(--ink-soft); }
  .nutrition__foot { border-top: 1px solid var(--ink-soft); margin-top: 6px; padding-top: 4px; font-size: 10px; line-height: 13px; }

  .distributor {
    position: absolute; left: 912px; top: 470px; width: 270px;
    font-family: "Signika", sans-serif; font-weight: 300; font-size: 19.5px; line-height: 30px;
  }
  .badges { position: absolute; left: 894px; top: 586px; width: 190px; height: 70px; }
</style>
</head>
<body>
<main class="label">
  <div class="band band--top"></div>
  <div class="band band--bottom"></div>
  <div class="band band--bottom-thin"></div>

  <header class="brand-tab">
    <svg width="404" height="124" viewBox="0 0 404 124">
      <path d="M0 0 H404 L392 16 V98 Q392 118 372 118 H32 Q12 118 12 98 V16 Z" fill="var(--gold)"/>
      <path d="M0 0 L12 16 V0 Z M404 0 L392 16 V0 Z" fill="var(--gold-deep)"/>
      <path d="M22 8 V96 Q22 108 34 108 H370 Q382 108 382 96 V8" fill="none" stroke="var(--brown)" stroke-width="2" stroke-dasharray="5 4"/>
    </svg>
    <div class="brand-name">Greenfold</div>
  </header>

  <p class="info info--story">This organic red rice is 100% sourced from families farming around the remote unpolluted lands in the Himalayans in Bhutan. Chemical preservatives free, Gluten free, Mineral rich, Organic Red Rice is the healthiest choice for you and your loved ones.</p>
  <p class="info info--storage">Store in a cool and dry place</p>
  <p class="info info--ingredients">Ingredients: Organic Bhutanese Red Rice</p>
  <p class="info info--weight">Net Weight 500gm<br>Best before-<span class="best-before">31/12/19</span></p>
  <p class="info info--origin">Product of Bhutan</p>

  <svg class="flag" role="img" aria-label="Flag of Bhutan with the thunder dragon" viewBox="0 0 206 103">
    <polygon points="0,0 206,0 0,103" fill="var(--flag-yellow)"/>
    <polygon points="206,0 206,103 0,103" fill="var(--flag-red)"/>
  </svg>

  <h1 class="product-title">Organic<br>Red Rice</h1>
  <div class="product-title-cn" lang="zh">有机红米</div>
  <div class="product-sub">Organic Bhutanese<span class="divider"></span>Red Rice</div>
  <div class="net-weight">Net Weight 500gm</div>

  <section class="nutrition" aria-label="Nutrition Facts">
    <div class="nutrition__title">Nutrition Facts</div>
    <div>Serving Size 1/4 cup (48g)</div>
    <div class="nutrition__bar nutrition__bar--thick"></div>
    <div class="nutrition__small"><b>Amount Per Serving</b></div>
    <div class="nutrition__row"><span><b>Calories</b> 170</span><span>Calories from Fat 5</span></div>
    <div class="nutrition__bar nutrition__bar--mid"></div>
    <div class="nutrition__dv">% Daily Value*</div>
    <div class="nutrition__row"><span><b>Total Fat</b> 1g</span><b>1%</b></div>
    <div class="nutrition__row"><span><b>Sodium</b> 0mg</span><b>0%</b></div>
    <div class="nutrition__row"><span><b>Total Carbohydrate</b> 37g</span><b>12%</b></div>
    <div class="nutrition__row nutrition__row--indent"><span>Fiber 2g</span><b>9%</b></div>
    <div class="nutrition__row nutrition__row--plain"><span><b>Protein</b> 4g</span><span></span></div>
    <div class="nutrition__bar nutrition__bar--thick"></div>
    <div class="nutrition__small">Not a significant source of saturated fat, trans fat, cholesterol, sugars, vitamin A, vitamin C, calcium and iron.</div>
    <div class="nutrition__foot">*Percent Daily Values are based on a 2,000 calorie diet.</div>
  </section>

  <p class="distributor">Distributed by Greenfold<br>27 Maple Crest Road<br>Singapore 600123</p>

  <svg class="badges" viewBox="0 0 190 70" aria-hidden="true">
    <circle cx="33" cy="32" r="29" fill="none" stroke="var(--ink)" stroke-width="2"/>
    <circle cx="151" cy="32" r="29" fill="none" stroke="var(--ink)" stroke-width="2"/>
  </svg>
</main>
</body>
</html>
```